Industry automation wholesale website

www.velqora.eu provides solutions for automation, building automation and digital signage.

Our products are rugged, reliable, energy saving and representative.

Scope of pages:
● welcome page
- scope of products
- applications, success stories and news
● category page
- short introduction
- sub categories
- product highlights
● product page
- short introduction
- about 3 to 4 pictures
- technical specifications: materials, dimensions
- price
- related products

Optional:
● contact page
- address
- contact form
● blog
- picture
- text
● logo
● favicon / apple touch icon

Conclusion:
● We need a professionally looking site
● Bright colors (e.g. white, grey, metalic colors, blue)

some pages we like:
http://www.brundafel.de/
http://www.korvimash.de/

Target Market(s)

Our target market is the industrial sector
● Target audience: engineering and IT professionals

Industry/Entity Type

Building

Requirements
Must have
• ● only use free available fonts e.g. Pellor Type Library (http://www.pellortype.com/webfonts)
Should not have
• ● sound
● flash

```html
<!DOCTYPE html>
<html lang="en">
<head>
<meta charset="utf-8">
<title>velqora – analog digital measurements</title>
<link href="https://fonts.googleapis.com/css2?family=Signika:wght@300;400;600&family=Ubuntu:wght@400&display=swap" rel="stylesheet">
<style>
:root{
  --dark:#34515f;
  --dark-2:#2b4553;
  --blue:#0e90d8;
  --blue-light:#1b9be0;
  --orange:#f07a12;
  --panel:#f1f1f1;
  --text:#333;
  --muted:#555;
  --white:#fff;
  --line:#c9d3d8;
}
*{margin:0;padding:0;box-sizing:border-box}
html,body{width:1097px;height:1200px;overflow:hidden}
body{position:relative;background:var(--white);font-family:"Signika",sans-serif;color:var(--text)}
.abs{position:absolute}
.header{left:0;top:0;width:1097px;height:105px;background:linear-gradient(90deg,#2f4b58,#4a6774 40%,#2f4b58)}
.backdrop{left:0;top:147px;width:1097px;height:425px;background:repeating-linear-gradient(135deg,#3b5663 0 3px,#2e4855 3px 6px)}
.brand{left:174px;top:14px;color:var(--white)}
.brand-name{font-family:"Ubuntu",sans-serif;font-size:52px;font-weight:400;line-height:1;letter-spacing:1px}
.brand-tag{font-size:13px;margin-top:2px;letter-spacing:.2px}
.lang{left:598px;top:69px;display:flex;align-items:center;gap:8px;color:var(--blue-light);font-style:italic;font-weight:600;font-size:15px}
.lang-box{width:21px;height:18px;background:var(--blue);display:flex;align-items:center;justify-content:center}
.cart{left:806px;top:60px;display:flex;align-items:center;gap:6px;color:var(--blue-light);font-style:italic;font-weight:600;font-size:14px}
.nav{left:0;top:105px;width:1097px;height:42px;background:linear-gradient(#fafafa,#e6e6e6)}
.nav a{position:absolute;top:0;height:42px;line-height:44px;font-family:"Ubuntu",sans-serif;font-size:14px;color:#111;text-decoration:none}
.nav a.active{background:var(--blue);color:var(--white);padding:0 9px}
.search-label{left:718px;top:117px;color:var(--blue);font-style:italic;font-weight:600;font-size:14px}
.search{left:778px;top:113px;width:159px;height:25px;border:1px solid var(--blue);background:var(--white)}
.sheet{left:135px;top:167px;width:826px;height:858px;background:var(--white);border:2px solid #c8c8c8;border-bottom:none}
.hero{left:161px;top:187px;width:775px;height:257px;background:linear-gradient(120deg,#cfd6da,#8a9aa2 45%,#6d7b83 70%,#b8c2c6)}
.dots{left:741px;top:406px;display:flex;gap:11px}
.dots span{width:17px;height:17px;background:#c98a74;border:1px solid #fff}
.dots span.on{background:var(--blue)}
.products-title{left:166px;top:451px;font-size:19px;color:#333;width:295px;border-bottom:2px dotted var(--blue);padding-bottom:0}
.products-title b{color:var(--blue);font-weight:400}
.product{width:81px;text-align:center;font-size:10.5px;font-style:italic;line-height:12px;color:#222}
.thumb{width:81px;height:59px;border:3px solid var(--blue);background:var(--white);margin-bottom:7px;display:flex;align-items:center;justify-content:center}
.thumb i{display:block;width:44px;height:32px;border-radius:3px}
.more{left:612px;top:655px;width:69px;height:25px;background:var(--orange);color:#fff;border-radius:5px;text-align:center;line-height:26px;font-weight:600;font-size:15px}
.card{background:var(--panel);border:1px solid #9fc7e0}
.card-head{background:var(--blue);color:var(--white);display:flex;align-items:center;justify-content:center;gap:14px;font-size:20px}
.testimonial{left:708px;top:456px;width:229px;height:241px}
.testimonial .card-head{height:36px;font-size:19px}
.testimonial p{position:absolute;left:40px;top:56px;width:180px;font-size:10.5px;font-style:italic;text-transform:uppercase;line-height:20.5px;color:#333}
.quote-big{position:absolute;left:6px;top:38px;font-size:54px;color:#c5c5c5;font-family:Georgia,serif;line-height:1}
.info{top:714px;width:229px;height:290px}
.info .card-head{height:53px}
.info .body{padding:14px 16px;font-size:12.3px;font-style:italic;line-height:17.1px;text-align:justify;color:#333;font-weight:300}
.news-item{padding:6px 18px 0 18px}
.news-date{color:var(--orange);font-size:10.5px;font-style:italic;font-weight:600}
.news-quote{display:flex;gap:6px;margin-top:8px;font-size:9.8px;font-style:italic;line-height:12px}
.news-quote span.q{font-family:Georgia,serif;font-size:22px;line-height:16px;color:#333}
.news-author{color:var(--blue);font-size:11px;font-weight:600;margin:12px 0 0 23px}
.news-sep{border-top:1px dotted #777;margin:12px 18px 0}
.footer{left:0;top:1025px;width:1097px;height:175px;background:linear-gradient(#2e4a57,#4d6773)}
.contact-line{display:flex;align-items:center;gap:12px;color:#fff;font-size:19px}
.footer-nav{left:162px;top:1137px;display:flex;gap:17px;color:#fff;font-size:9.5px;font-family:"Ubuntu",sans-serif}
.copyright{left:162px;top:1159px;color:#fff;font-size:8.5px;font-family:"Ubuntu",sans-serif}
.footer-brand{left:491px;top:1133px;color:#8796a0;font-family:"Ubuntu",sans-serif;font-size:30px}
.map{left:713px;top:1047px;width:221px;height:127px;background:radial-gradient(ellipse at center,#e3e6e8,#c5ccd0 60%,transparent 72%)}
</style>
</head>
<body>
<div class="abs header"></div>
<div class="abs backdrop"></div>

<div class="abs brand">
  <div class="brand-name">velqora</div>
  <div class="brand-tag">analog digital measurements</div>
</div>

<div class="abs lang"><span class="lang-box"><svg width="10" height="8" viewBox="0 0 10 8"><path d="M0 0h10L5 8z" fill="#fff"/></svg></span>ENGLISH</div>
<div class="abs cart">
  <svg width="32" height="28" viewBox="0 0 32 28" fill="none" stroke="#fff" stroke-width="2"><path d="M1 4h5l4 14h15l4-10H8"/><circle cx="12" cy="23" r="2.2"/><circle cx="23" cy="23" r="2.2"/></svg>
  Shopping cart
</div>

<nav class="abs nav">
  <a class="active" href="#" style="left:161px">HOME</a>
  <a href="#" style="left:236px">CATEGORY</a>
  <a href="#" style="left:330px">PRODUCT</a>
  <a href="#" style="left:418px">BLOG</a>
  <a href="#" style="left:480px">CONTACT</a>
</nav>
<div class="abs search-label">SEARCH</div>
<div class="abs search">
  <svg class="abs" style="right:8px;top:4px" width="17" height="17" viewBox="0 0 17 17" fill="none" stroke="#888" stroke-width="2"><circle cx="7" cy="7" r="5.5"/><path d="M11 11l5 5"/></svg>
</div>

<div class="abs sheet"></div>
<div class="abs hero" role="img" aria-label="Photo of industrial measurement displays in a plant"></div>
<div class="abs dots"><span class="on"></span><span></span><span></span><span></span></div>

<h2 class="abs products-title"><b>Our</b> Products</h2>

<div class="abs product" style="left:166px;top:484px"><div class="thumb" role="img" aria-label="Converter product photo"><i style="background:#4f8fc9"></i></div>RS422 / RS485 Converter</div>
<div class="abs product" style="left:274px;top:484px"><div class="thumb" role="img" aria-label="Repeater product photo"><i style="background:#5a7497"></i></div>RS422 / RS485 Repeater</div>
<div class="abs product" style="left:382px;top:484px"><div class="thumb" role="img" aria-label="Remote IO product photo"><i style="background:#5a7497"></i></div>RS485 Remote IO</div>
<div class="abs product" style="left:491px;top:484px"><div class="thumb" role="img" aria-label="Modbus IO product photo"><i style="background:#5a7497"></i></div>RS485 Modbus IO</div>
<div class="abs product" style="left:599px;top:484px"><div class="thumb" role="img" aria-label="Embedded system product photo"><i style="background:#3c6fa8;width:30px;height:40px"></i></div>Embedded Systems</div>
<div class="abs product" style="left:166px;top:589px"><div class="thumb" role="img" aria-label="PCI card product photo"><i style="background:#b2583a;height:22px"></i></div>PCI-Series</div>
<div class="abs product" style="left:274px;top:589px"><div class="thumb" role="img" aria-label="Industry PC product photo"><i style="background:#c9d1d8"></i></div>Industry PC</div>
<div class="abs product" style="left:382px;top:589px"><div class="thumb" role="img" aria-label="Industrial display product photo"><i style="background:#2a2a2a"></i></div>Industrial Display</div>
<div class="abs product" style="left:491px;top:589px"><div class="thumb" role="img" aria-label="Din rail power supply product photo"><i style="background:#9a9ea2;width:36px;height:40px"></i></div>Din Rail Power Supply</div>
<div class="abs more">MORE</div>

<section class="abs card testimonial">
  <div class="card-head">
    <svg width="16" height="26" viewBox="0 0 16 26" fill="#333"><path d="M5 0h6v9H5z"/><circle cx="8" cy="18" r="7"/></svg>
    Testimonial
  </div>
  <span class="quote-big">“</span>
  <p>Lorem ipsum is simply dummy text of the printing and type-setting industry. Lorem ipsum has been the industry's standard dummy text ever since the 1500s, when an unknown printer took a galley of type and scrambled it to</p>
</section>

<section class="abs card info" style="left:161px">
  <div class="card-head">
    <svg width="34" height="44" viewBox="0 0 34 44" fill="#333"><circle cx="22" cy="12" r="8"/><circle cx="10" cy="32" r="8"/><circle cx="22" cy="12" r="3" fill="#0e90d8"/><circle cx="10" cy="32" r="3" fill="#0e90d8"/></svg>
    Applications
  </div>
  <div class="body">Lorem Ipsum is simply dummy text of the printing and typesetting industry. Lorem Ipsum has been the industry's standard dummy text ever since the 1500s, when an unknown printer took a galley of type and scrambled it to make a type specimen book. It has survived not only five centuries, but also the leap into electronic typesetting, remaining essentially unchanged.</div>
</section>

<section class="abs card info" style="left:436px">
  <div class="card-head">
    <svg width="44" height="44" viewBox="0 0 44 44" fill="none" stroke="#333" stroke-width="3"><rect x="4" y="8" width="36" height="22"/><path d="M2 8h40M10 30l-3 12M34 30l3 12M12 24l8-8 6 5 8-9"/></svg>
    Success Stories
  </div>
  <div class="body">Lorem Ipsum is simply dummy text of the printing and typesetting industry. Lorem Ipsum has been the industry's standard dummy text ever since the 1500s, when an unknown printer took a galley of type and scrambled it to make a type specimen book. It has survived not only five centuries, but also the leap into electronic typesetting, remaining essentially unchanged.</div>
</section>

<section class="abs card info" style="left:709px">
  <div class="card-head">
    <svg width="42" height="44" viewBox="0 0 42 44" fill="none" stroke="#333" stroke-width="2.5"><rect x="8" y="2" width="32" height="40"/><path d="M8 10H2v30a2 2 0 0 0 6 0M14 10h20M14 18h8v8h-8zM26 18h8M26 24h8M14 32h20"/></svg>
    Latest News
  </div>
  <div class="news-item">
    <div class="news-date">{NOVEMBER 11, 2014}</div>
    <div class="news-quote"><span class="q">“</span><span>Lorem Ipsum is simply dummy text of the printing and typesetting industry."</span></div>
    <div class="news-author">Delan Petrov, Norvane Inc.</div>
  </div>
  <div class="news-sep"></div>
  <div class="news-item" style="padding-top:8px">
    <div class="news-date">{NOVEMBER 11, 2014}</div>
    <div class="news-quote"><span class="q">“</span><span>Lorem Ipsum is simply dummy text of the printing and typesetting industry."</span></div>
    <div class="news-author">Delan Petrov, Norvane Inc.</div>
  </div>
</section>

<footer class="abs footer"></footer>
<div class="abs contact-line" style="left:162px;top:1052px">
  <svg width="30" height="22" viewBox="0 0 30 22"><rect width="30" height="22" fill="#0e90d8"/><path d="M0 0l15 12L30 0" fill="none" stroke="#fff" stroke-width="2"/></svg>
  info@velqora.de
</div>
<div class="abs contact-line" style="left:162px;top:1091px;font-weight:600">
  <svg width="30" height="30" viewBox="0 0 30 30" fill="none" stroke="#0e90d8" stroke-width="2"><circle cx="15" cy="15" r="13.5"/><path d="M10 8l3 0 1 4-2 2c1 2 3 4 5 5l2-2 4 1v3c-7 1-14-6-13-13z" fill="#0e90d8" stroke="none"/></svg>
  +49-211-5550142
</div>
<div class="abs footer-nav"><span>HOME</span><span>CATEGORY</span><span>PRODUCT</span><span>BLOG</span><span>CONTACT</span></div>
<div class="abs copyright">COPYRIGHT@VELQORA.COM ALL RESERVED</div>
<div class="abs footer-brand">velqora</div>
<div class="abs map" role="img" aria-label="World map illustration"></div>
</body>
</html>
```